New Chartered Accounting Practice Needs Stationery Design

I need a new set of stationery including letterhead, business cards, envelopes and with compliments slips for a new Chartered Accounting Practice based in Melbourne, Victoria, Australia called "Marcus T. Hollinrake, Chartered Accountant".
I will be providing Taxation Services, Accounting Services, Self-Managed Superannuation Fund Consulting and general consulting advice to small and medium business enterprises. I would like to see designs that use the colour blue. The final design should communicate trust, technical expertise and security.
Target Market(s)
English speaking, Australians. Proprietors of small and medium businesses - aged 30-65. Fellow professionals - lawyers, investment consultants, other accountants. Retirees - aged 60 and over
Industry/Entity Type
Business
Look and feel
Each slider illustrates characteristics of the customer's brand and the style your logo design should communicate.

```html
<!DOCTYPE html>
<html lang="en">
<head>
<meta charset="utf-8">
<title>Marcus T. Hollinrake, Chartered Accountant – Letterhead</title>
<link href="https://fonts.googleapis.com/css2?family=Marcellus&family=Open+Sans:wght@400&display=swap" rel="stylesheet">
<style>
  :root {
    --navy: #00309a;
    --sky: #63b0e8;
    --ink: #0b1a3a;
    --brand-blue: #0a3aa8;
    --paper: #ffffff;
  }
  html, body {
    margin: 0;
    padding: 0;
    overflow: hidden;
    background: var(--paper);
  }
  .letterhead {
    position: relative;
    width: 927px;
    height: 1200px;
    background: var(--paper);
    overflow: hidden;
    font-family: "Open Sans", sans-serif;
  }
  .top-band {
    position: absolute;
    left: 0;
    top: 0;
    width: 927px;
    height: 64px;
  }
  .brand {
    position: absolute;
    left: 59px;
    top: 82px;
  }
  .brand-square {
    position: absolute;
    left: 0;
    top: 0;
    width: 84px;
    height: 110px;
    background: var(--navy);
  }
  .brand-name {
    position: absolute;
    left: 100px;
    top: 20px;
    margin: 0;
    white-space: nowrap;
    font-family: "Marcellus", serif;
    font-weight: 400;
    font-size: 31px;
    letter-spacing: 0.5px;
    text-transform: uppercase;
    color: var(--ink);
    line-height: 1;
  }
  .brand-tagline {
    position: absolute;
    left: 125px;
    top: 61px;
    margin: 0;
    white-space: nowrap;
    font-family: "Marcellus", serif;
    font-size: 25px;
    color: var(--brand-blue);
    line-height: 1;
  }
  .footer {
    position: absolute;
    left: 0;
    top: 1108px;
    width: 927px;
    height: 92px;
  }
  .footer-accent {
    position: absolute;
    left: 0;
    top: 0;
    width: 100%;
    height: 14px;
    background: var(--sky);
  }
  .footer-base {
    position: absolute;
    left: 0;
    top: 16px;
    width: 100%;
    height: 76px;
    background: var(--navy);
  }
  .contact {
    position: absolute;
    color: #fff;
    font-size: 14.8px;
    line-height: 19px;
    white-space: nowrap;
  }
  .contact svg {
    position: absolute;
    fill: #fff;
  }
  .contact-office { left: 54px; top: 1033px; }
  .contact-office .text { padding-left: 21px; margin-top: 106px; }
  .contact-line {
    position: absolute;
    color: #fff;
    font-size: 14.8px;
    line-height: 1;
    white-space: nowrap;
  }
  .icon {
    position: absolute;
  }
</style>
</head>
<body>
<main class="letterhead">

  <svg class="top-band" viewBox="0 0 927 64" aria-hidden="true">
    <rect x="0" y="0" width="927" height="31" fill="var(--navy)"/>
    <path d="M584 30 L813 30 L805 45 Q796 63 772 63 L625 63 Q601 63 592 45 Z" fill="var(--navy)"/>
  </svg>

  <header class="brand">
    <div class="brand-square" aria-hidden="true"></div>
    <h1 class="brand-name">Marcus T. Hollinrake</h1>
    <p class="brand-tagline">Chartered Accountant</p>
  </header>

  <footer class="footer">
    <div class="footer-accent"></div>
    <div class="footer-base"></div>
  </footer>

  <!-- Office address -->
  <svg class="icon" style="left:54px;top:1139px" width="15" height="20" viewBox="0 0 15 20" aria-hidden="true">
    <path d="M7.5 0C3.4 0 0 3.3 0 7.4 0 12.5 7.5 20 7.5 20S15 12.5 15 7.4C15 3.3 11.6 0 7.5 0Zm0 10.4a3 3 0 1 1 0-6 3 3 0 0 1 0 6Z" fill="#fff"/>
  </svg>
  <div class="contact-line" style="left:75px;top:1142px">Office : 18 Carrick Lane,</div>
  <div class="contact-line" style="left:75px;top:1161px">Elmwood VIC 3190</div>

  <!-- Phone and fax -->
  <svg class="icon" style="left:363px;top:1137px" width="17" height="13" viewBox="0 0 17 13" aria-hidden="true">
    <path d="M0 4.5C0 1.5 4 0 8.5 0S17 1.5 17 4.5v1.3h-4.3V3.6H4.3v2.2H0Z" fill="#fff"/>
    <path d="M3 7.5 5.2 4.6h6.6L14 7.5V13H3Z" fill="#fff"/>
  </svg>
  <div class="contact-line" style="left:390px;top:1138px">Phone : 0400 118 263</div>

  <svg class="icon" style="left:363px;top:1161px" width="17" height="15" viewBox="0 0 17 15" aria-hidden="true">
    <rect x="4" y="0" width="9" height="4" fill="#fff"/>
    <rect x="0" y="5" width="17" height="6" rx="1.5" fill="#fff"/>
    <rect x="4" y="10" width="9" height="5" fill="#fff"/>
    <rect x="5.5" y="11.5" width="6" height="1" fill="var(--navy)"/>
  </svg>
  <div class="contact-line" style="left:390px;top:1162px">Fax: (03) 9000 4172</div>

  <!-- Postal and email -->
  <svg class="icon" style="left:630px;top:1138px" width="19" height="13" viewBox="0 0 19 13" aria-hidden="true">
    <rect x="0.75" y="0.75" width="17.5" height="11.5" fill="none" stroke="#fff" stroke-width="1.5"/>
    <rect x="11" y="3" width="5" height="3.5" fill="#fff"/>
    <rect x="3" y="7.5" width="8" height="1.2" fill="#fff"/>
  </svg>
  <div class="contact-line" style="left:656px;top:1137px">PO Box 4406, Elmwood VIC 3190</div>

  <svg class="icon" style="left:632px;top:1164px" width="16" height="11" viewBox="0 0 16 11" aria-hidden="true">
    <rect x="0" y="0" width="16" height="11" rx="1.5" fill="#fff"/>
    <path d="M0.5 0.8 8 6.5 15.5 0.8" fill="none" stroke="var(--navy)" stroke-width="1.4"/>
  </svg>
  <div class="contact-line" style="left:658px;top:1163px">marcus.hollinrake@ledgermail.com</div>

</main>
</body>
</html>
```